Brightwell Support! Virtual Assistant business needs a Website

I have started an online business called "Brightwell Support". I offer all the same types of services as a typical Personal Assistant, only remotely. For example, document formatting and editing (word, powerpoint, excel etc.), email and calendar management, appointments and bookings, document creation, reports, travel and event management and so on.

I already have a logo ready to go, however I have yet to finalise the copy for the site, so if you could create the pages with pictures, and I can fill in the wording at a later date.

Target Market(s)

Anyone who is overloaded at work and needs someone to take the admin work off their hands.

Number of Pages Required

4 page

Font styles to use
Sans Serif
Script
Other font styles liked:
• Gotham Medium is used in my font

Colors

Designer to choose colors to be used in the design.

Requirements
Must have
• Home Page
• About Page
• Pricing Page
• Contact Page
Nice to have
• Pictures and a professional design, I like white space and simple design.
Should not have
• cartoons or anything unprofessional looking.

```html
<!DOCTYPE html>
<html lang="en">
<head>
<meta charset="utf-8">
<title>Brightwell Support</title>
<link rel="stylesheet" href="https://fonts.googleapis.com/css2?family=Montserrat:wght@500;600;700&family=Open+Sans:wght@400;600;700&family=Poppins:wght@400;500&display=swap">
<style>
:root{
  --blue:#2f6ab5;
  --blue-deep:#1f5496;
  --navy:#1d4f8c;
  --accent:#4270d0;
  --ink:#333;
  --muted:#555;
  --white:#fff;
  --footer:#4b4b4b;
  --line:#2a5ea8;
}
*{box-sizing:border-box;margin:0;padding:0}
html,body{width:706px;height:1200px;overflow:hidden;background:var(--white)}
body{position:relative;font-family:"Open Sans",Arial,sans-serif;color:var(--ink)}
.abs{position:absolute}

/* header */
.site-header{position:absolute;left:0;top:0;width:706px;height:57px;background:var(--white);box-shadow:0 1px 3px rgba(0,0,0,.08);z-index:2}
.topbar{position:absolute;right:0;top:0;width:383px;height:27px;background:var(--blue-deep);clip-path:polygon(0 0,100% 0,100% 100%,44px 100%)}
.topbar-item{position:absolute;top:7px;font:500 8px "Poppins",sans-serif;color:var(--white);display:flex;align-items:center;gap:4px}
.topbar-sep{position:absolute;top:7px;left:537px;color:var(--white);font-size:8px}
.brand{position:absolute;left:69px;top:14px;display:flex;align-items:center;gap:7px}
.brand-mark{width:28px;height:28px;border-radius:50%;background:var(--navy)}
.brand-name{font:600 15px "Montserrat",sans-serif;color:var(--navy);letter-spacing:.5px}
.main-nav{position:absolute;top:37px;font:500 9px "Poppins",sans-serif;color:#222}
.main-nav span{position:absolute;white-space:nowrap}

/* hero */
.hero{position:absolute;left:0;top:57px;width:706px;height:277px;background:radial-gradient(circle at 70% 40%,#3a77c4,var(--blue) 60%,#2a5fa8)}
.hero-photo{position:absolute;left:48px;top:52px;width:196px;height:196px;border-radius:50%;background:linear-gradient(135deg,#eef1f5,#c9d2dc);border:3px solid var(--white)}
.hero-photo-small{position:absolute;left:153px;top:35px;width:82px;height:82px;border-radius:50%;background:linear-gradient(135deg,#d8dde3,#9aa4ae);border:3px solid var(--white)}
.hero-kicker{position:absolute;left:280px;top:69px;font:400 16px "Open Sans",sans-serif;color:var(--white)}
.hero-title{position:absolute;left:280px;top:92px;font:700 29px "Montserrat",sans-serif;color:var(--white);letter-spacing:.3px}
.hero-sub{position:absolute;left:279px;top:134px;font:400 13.5px "Open Sans",sans-serif;color:var(--white)}
.btn-outline{position:absolute;left:280px;top:174px;width:99px;height:31px;border:1.5px solid var(--white);border-radius:4px;color:var(--white);font:600 10px "Open Sans",sans-serif;display:flex;align-items:center;justify-content:center}
.dots{position:absolute;display:flex;gap:2px}
.dots i{display:block;width:6px;height:6px;border-radius:50%;border:1px solid var(--white)}
.dots i.on{background:var(--white)}

/* about */
.about-photo{position:absolute;left:69px;top:393px;width:267px;height:152px;background:linear-gradient(135deg,#c9b8a2,#8a6d52)}
.about-ghost{position:absolute;left:384px;top:384px;font:400 44px "Montserrat",sans-serif;color:#e6ebf2;letter-spacing:2px}
.about-title{position:absolute;left:381px;top:405px;font:700 16px "Open Sans",sans-serif;color:var(--ink)}
.about-text{position:absolute;left:381px;top:440px;width:250px;font:400 6.6px/14.6px "Open Sans",sans-serif;color:var(--muted);text-align:justify}
.btn-solid{position:absolute;left:378px;top:514px;width:74px;height:26px;background:var(--navy);border-radius:6px;color:var(--white);font:700 9px "Open Sans",sans-serif;display:flex;align-items:center;justify-content:center}

/* services */
.services{position:absolute;left:0;top:606px;width:706px;height:232px;background:linear-gradient(180deg,#275ea6,#2d69b3)}
.services-ghost{position:absolute;left:10px;top:84px;font:400 38px "Open Sans",sans-serif;color:rgba(255,255,255,.12)}
.services-title{position:absolute;left:18px;top:103px;font:700 16.5px "Open Sans",sans-serif;color:var(--white)}
.service-card{position:absolute;top:52px;width:116px;height:118px;background:var(--white);display:flex;flex-direction:column;align-items:center;padding-top:20px}
.service-card.active{background:var(--accent);box-shadow:0 4px 10px rgba(0,0,0,.2)}
.service-card svg{width:48px;height:48px}
.service-name{margin-top:10px;font:700 9px/12.5px "Open Sans",sans-serif;color:#222;text-align:center}
.service-card.active .service-name{color:var(--white)}

/* subscribe */
.subscribe-title{position:absolute;left:62px;top:897px;width:200px;text-align:center;font:700 15px "Open Sans",sans-serif;color:var(--ink)}
.subscribe-sub{position:absolute;left:62px;top:925px;width:200px;text-align:center;font:400 9px "Open Sans",sans-serif;color:var(--muted)}
.email-field{position:absolute;left:67px;top:961px;width:190px;height:18px;border-bottom:1px dashed var(--line);display:flex;align-items:center;justify-content:center;gap:14px;font:400 10px "Open Sans",sans-serif;color:#666}
.btn-subscribe{position:absolute;left:125px;top:993px;width:75px;height:24px;background:var(--navy);color:var(--white);font:700 9px "Open Sans",sans-serif;display:flex;align-items:center;justify-content:center}
.cta{position:absolute;left:324px;top:896px;width:313px;height:125px;background:linear-gradient(135deg,#8c8c8c,#4f4f4f)}
.cta-title{position:absolute;left:0;top:49px;width:100%;text-align:center;font:700 16px "Open Sans",sans-serif;color:var(--white);text-shadow:0 1px 3px rgba(0,0,0,.5)}
.cta-btn{position:absolute;left:123px;top:82px;width:72px;height:20px;border:1px solid var(--white);color:var(--white);font:600 9.5px "Open Sans",sans-serif;display:flex;align-items:center;justify-content:center}

/* footer */
.site-footer{position:absolute;left:0;top:1083px;width:706px;height:117px;background:var(--footer)}
.footer-nav{position:absolute;top:46px;font:500 8.5px "Poppins",sans-serif;color:var(--white)}
.footer-nav span{position:absolute;white-space:nowrap}
.social{position:absolute;top:40px;display:flex;gap:7px;left:511px}
.social i{display:block;width:20px;height:20px;border-radius:50%;border:1px solid var(--white)}
.footer-rule{position:absolute;left:68px;top:85px;width:570px;height:1px;background:rgba(255,255,255,.3)}
.footer-legal{position:absolute;top:96px;left:0;width:706px;text-align:center;font:400 7px "Open Sans",sans-serif;color:var(--white)}
</style>
</head>
<body>

<header class="site-header">
  <div class="topbar"></div>
  <div class="topbar-item" style="left:486px">
    <svg width="7" height="8" viewBox="0 0 7 8"><circle cx="3.5" cy="2" r="2" fill="#fff"/><path d="M0 8c0-2.5 1.5-3.5 3.5-3.5S7 5.5 7 8z" fill="#fff"/></svg>Login
  </div>
  <span class="topbar-sep">|</span>
  <div class="topbar-item" style="left:557px">
    <svg width="7" height="7" viewBox="0 0 10 10"><path d="M2 0l2 2.5-1.2 1.3c.6 1.4 1.6 2.4 3 3L7 5.6 10 7.6 8.6 10C4 9.6.4 6 0 1.4z" fill="#fff"/></svg>(+1) 555-010-0199
  </div>
  <div class="brand"><span class="brand-mark"></span><span class="brand-name">BRIGHTWELL SUPPORT</span></div>
  <nav class="main-nav">
    <span style="left:394px">Home</span>
    <span style="left:444px">About Us</span>
    <span style="left:506px">Pricing</span>
    <span style="left:559px">Contact Us</span>
    <svg style="position:absolute;left:631px;top:2px" width="8" height="8" viewBox="0 0 10 10"><circle cx="4" cy="4" r="3" stroke="#222" stroke-width="1.6" fill="none"/><path d="M6.3 6.3L9.3 9.3" stroke="#222" stroke-width="1.8"/></svg>
  </nav>
</header>

<section class="hero">
  <div class="hero-photo" role="img" aria-label="Photo of an assistant on the phone at an office desk"></div>
  <div class="hero-photo-small" role="img" aria-label="Photo of a smiling assistant with a phone"></div>
  <p class="hero-kicker">Work Smater With</p>
  <h1 class="hero-title">BRIGHTWELL SUPPORT</h1>
  <p class="hero-sub">I offer all types of Assistant services remotely</p>
  <div class="btn-outline">View Services</div>
  <div class="dots" style="left:339px;top:253px"><i class="on"></i><i></i><i></i><i></i></div>
</section>

<section class="about">
  <div class="about-photo" role="img" aria-label="Photo of a desk phone, coffee cup and a hand writing notes"></div>
  <div class="about-ghost">ABOUT</div>
  <h2 class="about-title">ABOUT US</h2>
  <p class="about-text">Lorem Ipsum is simply dummy text of the printing and typesetting industry. Lorem Ipsum has been the industry's standard dummy text ever since the 1500s, when an unknown printer took a galley of type and scrambled it to make a type specimen book.</p>
  <div class="btn-solid">Read More</div>
</section>

<section class="services">
  <div class="services-ghost">SERVICES</div>
  <h2 class="services-title">WHAT WE OFFER</h2>

  <div class="service-card" style="left:203px">
    <svg viewBox="0 0 48 48"><path d="M9 4h22v18M9 4v40h20" fill="none" stroke="var(--navy)" stroke-width="2.5"/><path d="M14 13h14M14 19h14M14 25h12M14 31h8" stroke="var(--navy)" stroke-width="2"/><path d="M27 36l5 5 10-11" fill="none" stroke="#111" stroke-width="3.5"/></svg>
    <div class="service-name">DOCUMENT<br>FORMATTING</div>
  </div>

  <div class="service-card active" style="left:330px">
    <svg viewBox="0 0 48 48"><rect x="4" y="8" width="40" height="34" rx="2" fill="none" stroke="#fff" stroke-width="2"/><path d="M4 15h40" stroke="#fff" stroke-width="2"/><path d="M13 4v8M35 4v8" stroke="#fff" stroke-width="2.5"/><path d="M9 20h4M17 20h4M27 20h4M35 20h4M9 26h4M35 26h4M9 32h4M35 32h4" stroke="#fff" stroke-width="2" stroke-dasharray="1.5 1"/><circle cx="24" cy="31" r="8" fill="var(--accent)" stroke="#fff" stroke-width="2"/><path d="M24 26v5h4" stroke="#fff" stroke-width="1.8" fill="none"/></svg>
    <div class="service-name">CALENDAR<br>MANAGEMENT</div>
  </div>

  <div class="service-card" style="left:456px">
    <svg viewBox="0 0 48 48"><path d="M14 10A18 18 0 1 1 12 40" fill="none" stroke="var(--navy)" stroke-width="4"/><path d="M10 4l5 7-8 2z" fill="var(--navy)"/><path d="M28 14v12l6 5" fill="none" stroke="var(--navy)" stroke-width="3"/><circle cx="14" cy="34" r="7" fill="none" stroke="#222" stroke-width="4" stroke-dasharray="3 2"/><circle cx="14" cy="34" r="4" fill="#222"/><circle cx="14" cy="34" r="1.6" fill="#fff"/></svg>
    <div class="service-name">APPOINTMENTS &amp;<br>BOOKINGS</div>
  </div>

  <div class="service-card" style="left:583px">
    <svg viewBox="0 0 48 48"><rect x="20" y="3" width="20" height="28" fill="#fff" stroke="var(--navy)" stroke-width="2"/><rect x="15" y="8" width="20" height="30" fill="#fff" stroke="var(--navy)" stroke-width="2"/><rect x="8" y="13" width="22" height="32" fill="#fff" stroke="#111" stroke-width="2.5"/><path d="M12 20h14M12 25h14M12 30h14M12 35h14M12 40h10" stroke="var(--navy)" stroke-width="1.6"/></svg>
    <div class="service-name">DOCUMENT<br>CREATION</div>
  </div>

  <div class="dots" style="left:439px;top:201px"><i class="on" style="width:5px;height:5px"></i><i style="width:5px;height:5px"></i><i style="width:5px;height:5px"></i><i style="width:5px;height:5px"></i></div>
</section>

<section class="subscribe">
  <h2 class="subscribe-title">SUBSCRIBE</h2>
  <p class="subscribe-sub">Get Notified about the next update</p>
  <div class="email-field">Enter your Email
    <svg width="10" height="8" viewBox="0 0 10 8"><rect width="10" height="8" rx="1" fill="var(--navy)"/><path d="M0 1l5 3.5L10 1" stroke="#fff" fill="none" stroke-width="1"/></svg>
  </div>
  <div class="btn-subscribe">Subscribe</div>
</section>

<aside class="cta" role="img" aria-label="Photo of two smiling men standing against a concrete wall">
  <p class="cta-title">Want To Know More??</p>
  <div class="cta-btn">Contact Us</div>
</aside>

<footer class="site-footer">
  <nav class="footer-nav">
    <span style="left:67px">Home</span>
    <span style="left:119px">About Us</span>
    <span style="left:184px">Pricing</span>
    <span style="left:240px">Contact Us</span>
  </nav>
  <div class="social"><i></i><i></i><i></i><i></i><i></i></div>
  <div class="footer-rule"></div>
  <p class="footer-legal">Copyrights © 2018. All Rights Reserved. &nbsp;&nbsp; | &nbsp;&nbsp; Private policy</p>
</footer>

</body>
</html>
```